Business card design needed

We are a gardening company who handle:
All Forms of gardens work including
Mowing
Pruning
edging
weeding
Poisoning
Landscaping
Minor Stump Removal
Rubbish Removal
and more

I want a card that look professional not cartoon style

Industry/Entity Type

Business

Contact Information for Business Card

Fernhollow Yard and Lawn Service

Greg Halden
0486152938

```html
<!DOCTYPE html>
<html lang="en">
<head>
<meta charset="utf-8">
<title>Fernhollow Yard and Lawn Service – Business Card</title>
<link rel="stylesheet" href="https://fonts.googleapis.com/css2?family=Questrial&display=swap">
<style>
  :root {
    --page-bg: #5e5a58;
    --card-bg: #ffffff;
    --card-shade: #eceded;
    --brand-green: #4dbb3c;
    --text-grey: #5a5a5a;
    --divider-grey: #8a8a8a;
  }
  html, body {
    margin: 0;
    padding: 0;
    width: 1200px;
    height: 871px;
    overflow: hidden;
    background: var(--page-bg);
  }
  .canvas {
    position: relative;
    width: 1200px;
    height: 871px;
  }
  .card {
    position: absolute;
    left: 150px;
    top: 178px;
    width: 900px;
    height: 514px;
    background: linear-gradient(135deg, var(--card-bg) 40%, var(--card-shade) 100%);
    box-shadow: 0 18px 40px rgba(0,0,0,0.35);
    font-family: "Questrial", "Century Gothic", sans-serif;
    color: var(--text-grey);
  }
  .card__band {
    position: absolute;
    left: 0;
    top: 0;
    width: 64px;
    height: 100%;
    background: var(--brand-green);
  }
  .card__person {
    position: absolute;
    top: 30px;
    right: 40px;
    margin: 0;
    font-size: 15px;
    letter-spacing: 0.5px;
    text-transform: uppercase;
  }
  .card__person-name { color: var(--brand-green); font-weight: 700; }
  .card__person-sep { color: var(--divider-grey); margin: 0 4px; }
  .card__company {
    position: absolute;
    left: 112px;
    top: 80px;
    margin: 0;
    font-size: 32px;
    font-weight: 400;
    letter-spacing: 1px;
    text-transform: uppercase;
    color: var(--brand-green);
  }
  .card__services {
    position: absolute;
    left: 112px;
    top: 128px;
    margin: 0;
    font-size: 18px;
    line-height: 24px;
  }
  .card__services .sep { color: var(--brand-green); margin: 0 4px; }
  .card__contacts {
    position: absolute;
    left: 300px;
    top: 300px;
    margin: 0;
    display: grid;
    grid-template-columns: auto auto;
    column-gap: 14px;
    row-gap: 2px;
    font-size: 19px;
    line-height: 25px;
  }
  .card__contacts dt { color: var(--brand-green); text-align: right; }
  .card__contacts dd { margin: 0; color: var(--text-grey); }
</style>
</head>
<body>
<main class="canvas">
  <article class="card">
    <div class="card__band"></div>
    <p class="card__person"><span class="card__person-name">Greg Halden</span><span class="card__person-sep">|</span>Managing Director</p>
    <h1 class="card__company">Fernhollow Yard and Lawn Service.</h1>
    <p class="card__services">
      Mowing<span class="sep">|</span>Pruning<span class="sep">|</span>Edging<span class="sep">|</span>Weeding<span class="sep">|</span>Poisoning<span class="sep">|</span>Landscaping<br>
      Minor Stump Removal<span class="sep">|</span>Rubbish Removal
    </p>
    <dl class="card__contacts">
      <dt>Address:</dt><dd>Birchline House, 12 Meadow Row, Ashford.</dd>
      <dt>Telephone:</dt><dd>1800 614 270, 1800 614 271</dd>
      <dt>Skype:</dt><dd>fernhollowyard</dd>
      <dt>E-Mail:</dt><dd>hello@fernhollowyard.com</dd>
      <dt>Web:</dt><dd>fernhollowyardandlawn.com</dd>
    </dl>
  </article>
</main>
</body>
</html>
```